Zertifikat-Design und Garantieschein-Design für Uhrenmanufaktur gesucht
Zielgruppe
Wir sind eine Uhrenmanufaktur und fertigen hochwertige mechanische Armbanduhren in größten Teilen in Handarbeit.
Für die Auslieferung unserer Uhren brauchen wir ein Zertifikat und einen Garantieschein (jeweils 1 Blatt).
Unsere Zielgruppe sind gutverdienende Menschen zwischen 25 und 55 Jahren.
Aufgabenstellung
Es soll jeweils ein Zertifikat erstellt werden (1 Blatt - nur Vorderseite) und ein Garantieschein (1 Blatt - Vorder- und Rückseite). Alle Vorgaben, sowie Bilder der Uhren als Inspiration sind in der PDF enthalten.

```html
<!DOCTYPE html>
<html lang="de">
<head>
<meta charset="utf-8">
<title>Fernwald Uhrmacher – Gebrauchsempfehlung</title>
<link href="https://fonts.googleapis.com/css2?family=Poppins:wght@300;400;500&display=swap" rel="stylesheet">
<style>
  :root {
    --bg: #e9e7e5;
    --frame: #e6a6c2;
    --frame-dark: #da86a8;
    --panel: #f4dde7;
    --ink: #2a2226;
    --accent: #a2397c;
  }
  * { box-sizing: border-box; margin: 0; padding: 0; }
  html, body {
    width: 1200px; height: 1188px; overflow: hidden;
    background: var(--bg);
    font-family: "Poppins", sans-serif;
    color: var(--ink);
  }
  .sheet {
    position: absolute; left: 164px; top: 24px;
    width: 872px; height: 1140px;
    background: linear-gradient(90deg, var(--frame), var(--frame-dark));
    padding: 30px 32px 34px;
  }
  .panel {
    position: relative;
    width: 100%; height: 100%;
    background: var(--panel);
    padding: 0 40px 0 46px;
  }
  .brand {
    position: absolute; left: 0; right: 0; top: 14px;
    text-align: center;
    font-weight: 300;
  }
  .brand-name {
    display: block;
    font-size: 52px; line-height: 1;
    letter-spacing: 1px;
  }
  .brand-sub {
    display: block;
    font-size: 22px; line-height: 1.2;
    letter-spacing: 3px;
    margin-top: 6px;
  }
  .care { position: absolute; left: 46px; right: 34px; }
  .care-de { top: 170px; }
  .care-en { top: 633px; }
  .section-title {
    font-size: 18.5px; font-weight: 400;
    letter-spacing: 0.2px;
    line-height: 24px;
    text-transform: uppercase;
    white-space: nowrap;
    margin-bottom: 20px;
  }
  .care-text {
    display: grid;
    grid-template-columns: 1fr 1fr;
    column-gap: 34px;
    font-size: 13.8px; font-weight: 300;
    line-height: 21px;
  }
  .care-text p { margin-bottom: 21px; }
  .care-text p:last-child { margin-bottom: 0; }
  .label { color: var(--accent); font-weight: 500; }
</style>
</head>
<body>
  <article class="sheet">
    <div class="panel">
      <header class="brand">
        <span class="brand-name">FERNWALD</span>
        <span class="brand-sub">UHRMACHER</span>
      </header>

      <section class="care care-de">
        <h2 class="section-title">Gebrauchsempfehlung zum Werterhalt der Uhr</h2>
        <div class="care-text">
          <div class="care-column">
            <p><span class="label">Headline:</span> Um einen möglichst stabilen Gang der Uhr zu erzielen, empfehlen wir die Uhr einmal innerhalb von 24 Stunden aufzuziehen. Dazu wird die Krone im Uhrzeigersinn solange zwischen Daumen und Zeigefinger gedreht, bis ein deutlicher Widerstand zu spüren ist. Die Uhr ist nun voll aufgezogen. Wird versucht mit deutlichem Kraftaufwand über diesen Punkt hinaus die Krone zu drehen, kann es in der Uhr zu Beschädigungen kommen.</p>
            <p><span class="label">Headline:</span> Wird die Uhr über einen längeren Zeitraum nicht getragen, sollte sie einmal im Monat aufgezogen werden, um das Verfestigen der Öle und Fette zu verhindern.</p>
            <p><span class="label">Headline:</span> Zum Stellen der Zeiger wird die Krone vom Gehäuse weggezogen, bis sie deutlich in der zweiten Position einrastet.</p>
          </div>
          <div class="care-column">
            <p>Dazu wird der Fingernagel auf der Unterseite in den Spalt zwischen Gehäuse und Krone geschoben und gleichzeitig an der Krone gezogen. Durch drehen der Krone werden nun die Zeiger in die gewünschte Position gebracht. Nach dem Zeigerstellen muss die Krone wieder in die Ausgangsposition gedrückt werden. Achtung! Bei gezogener Krone ist der Spritzwasserschutz nicht gegeben.</p>
            <p><span class="label">Headline:</span> Harte Erschütterungen oder Stöße, Untertauchen der Uhr unter Wasser, extreme Temperaturschwankungen, hohe Luftfeuchtigkeit oder die Nähe von größeren Magneten sollten vermieden werden.</p>
            <p><span class="label">Headline:</span> Um den Zuverlässigen Gang der Uhr zu gewährleisten, empfehlen wir den Service der Uhr aller 3 bis 5 Jahre in unserer Werkstatt.</p>
          </div>
        </div>
      </section>

      <section class="care care-en" lang="en">
        <h2 class="section-title">Usage recommendation to maintain the value of the watch</h2>
        <div class="care-text">
          <div class="care-column">
            <p><span class="label">Headline:</span> In order to achieve the accuracy of the watch, we recommend winding the watch once within 24 hours. To do this, turn the crown clockwise between thumb and forefinger until a clear resistance is felt. The watch is now fully wound. If an attempt is made to turn the crown with considerable force beyond this point, the watch may be damaged.</p>
            <p><span class="label">Headline:</span> If the watch is not worn for a long period of time, it should be wound once a month to prevent the oils and greases from solidifying.</p>
            <p><span class="label">Headline:</span> To set the hands, pull the crown away from the case until it clearly clicks into the second position. To do this, push the</p>
          </div>
          <div class="care-column">
            <p>fingernail on the bottom side into the gap between the case and the crown and pull the crown at the same time. By turning the crown, the hands are now brought into the desired position. After setting the hands, the crown must be pushed back into its original position. Attention. Splash water protection is not provided when the crown is pulled out.</p>
            <p><span class="label">Headline:</span> Hard shocks or impacts, submersion of the watch in water, extreme temperature fluctuations, high humidity or the proximity of larger magnets should be avoided.</p>
            <p><span class="label">Headline:</span> To ensure the reliable running of the watch, we recommend servicing the watch every 3 to 5 years in our workshop.</p>
          </div>
        </div>
      </section>
    </div>
  </article>
</body>
</html>
```